Corvane Bookkeeping Services business cards

looking for a double sided business card design. My logo is attached. I am looking for a design similar to the attached. Keen to see what my logo in white on the blue background would look like.

```html
<!DOCTYPE html>
<html lang="en">
<head>
<meta charset="utf-8">
<title>Corvane Bookkeeping Services – Business Cards</title>
<link href="https://fonts.googleapis.com/css2?family=Montserrat:wght@600;700;800&family=Open+Sans:wght@400;600&display=swap" rel="stylesheet">
<style>
  :root {
    --navy: #0b3670;
    --green: #8cb32b;
    --white: #ffffff;
    --ink: #3c3c3c;
    --backdrop: #e9e6e3;
  }
  * { margin: 0; padding: 0; box-sizing: border-box; }
  html, body { width: 1200px; height: 900px; overflow: hidden; }
  body {
    background: var(--backdrop);
    position: relative;
    font-family: "Open Sans", Arial, sans-serif;
  }
  .card {
    position: absolute;
    left: 240px;
    width: 720px;
    height: 411px;
    border-radius: 22px;
    box-shadow: 0 6px 18px rgba(0,0,0,0.18);
    overflow: hidden;
  }
  .card--front { top: 24px; background: var(--navy); }
  .card--back { top: 465px; background: var(--white); }

  .wordmark {
    position: absolute;
    display: flex;
    align-items: center;
    gap: 16px;
    font-family: "Montserrat", Arial, sans-serif;
    font-weight: 800;
  }
  .wordmark__square { flex: none; }
  .wordmark__name { line-height: 1.02; }

  .card--front .wordmark {
    left: 0; right: 0; top: 0; bottom: 0;
    justify-content: center;
    color: var(--white);
  }
  .card--front .wordmark__square { width: 56px; height: 56px; background: var(--white); }
  .card--front .wordmark__name { font-size: 40px; }
  .card--front .wordmark__name small { display: block; font-size: 18px; letter-spacing: 2px; text-transform: uppercase; }

  .card--back .wordmark {
    left: 48px; top: 176px;
    color: var(--navy);
    gap: 12px;
  }
  .card--back .wordmark__square { width: 38px; height: 38px; background: var(--navy); }
  .card--back .wordmark__name { font-size: 28px; }
  .card--back .wordmark__name small { display: block; font-size: 12px; letter-spacing: 1.5px; text-transform: uppercase; }

  .divider {
    position: absolute;
    left: 392px; top: 86px;
    width: 1.5px; height: 240px;
    background: var(--navy);
  }
  .contact {
    position: absolute;
    left: 420px; top: 84px;
  }
  .contact__name {
    font-family: "Montserrat", Arial, sans-serif;
    font-weight: 800;
    font-size: 25px;
    color: var(--navy);
    text-transform: uppercase;
    letter-spacing: 0.3px;
  }
  .contact__role {
    font-family: "Montserrat", Arial, sans-serif;
    font-weight: 700;
    font-size: 15px;
    color: var(--green);
    margin-bottom: 18px;
  }
  .contact__list { list-style: none; }
  .contact__item {
    display: flex;
    align-items: flex-start;
    gap: 12px;
    font-size: 15px;
    line-height: 1.4;
    color: var(--ink);
  }
  .contact__item + .contact__item { margin-top: 2px; }
  .contact__item--address { margin-bottom: 10px; }
  .contact__icon { width: 14px; height: 14px; flex: none; margin-top: 3px; fill: var(--green); }
</style>
</head>
<body>

<section class="card card--front" aria-label="Card front">
  <div class="wordmark">
    <span class="wordmark__square"></span>
    <span class="wordmark__name">Corvane<small>Bookkeeping Services</small></span>
  </div>
</section>

<section class="card card--back" aria-label="Card back">
  <div class="wordmark">
    <span class="wordmark__square"></span>
    <span class="wordmark__name">Corvane<small>Bookkeeping Services</small></span>
  </div>

  <div class="divider"></div>

  <div class="contact">
    <p class="contact__name">Elias Marlow</p>
    <p class="contact__role">Managing Director</p>
    <ul class="contact__list">
      <li class="contact__item contact__item--address">
        <svg class="contact__icon" viewBox="0 0 14 14"><path d="M7 0a5 5 0 0 0-5 5c0 3.6 5 9 5 9s5-5.4 5-9a5 5 0 0 0-5-5zm0 7a2 2 0 1 1 0-4 2 2 0 0 1 0 4z"/></svg>
        <span>48 Harlow Street, Suite 2<br>Westbridge, 204518</span>
      </li>
      <li class="contact__item">
        <svg class="contact__icon" viewBox="0 0 14 14"><path d="M3 1l2.2 2.8-1.3 1.6a8 8 0 0 0 3.7 3.7l1.6-1.3L12 10l-1.3 2.4C6 12.4 1.6 8 1.6 3.3z"/></svg>
        <span>044-555-210 348</span>
      </li>
      <li class="contact__item">
        <svg class="contact__icon" viewBox="0 0 14 14"><path d="M4 0h6a1 1 0 0 1 1 1v12a1 1 0 0 1-1 1H4a1 1 0 0 1-1-1V1a1 1 0 0 1 1-1zm.5 1.5v9.5h5V1.5z"/></svg>
        <span>044-555-210 349</span>
      </li>
      <li class="contact__item">
        <svg class="contact__icon" viewBox="0 0 14 14"><path d="M0 3h14v8H0zm1.2 1L7 8l5.8-4z"/></svg>
        <span>info@corvanebooks.com</span>
      </li>
      <li class="contact__item">
        <svg class="contact__icon" viewBox="0 0 14 14"><circle cx="7" cy="7" r="6.5"/></svg>
        <span>www.corvanebooks.com</span>
      </li>
    </ul>
  </div>
</section>

</body>
</html>
```